velmar qt 450 2022 Vehicle Warp

Wrap Velmar QT 450 2022 with the company Brookvale Security I have attached pictures of our new trucks of our sister company Brookvale locksmith and Brookvale Lock Auto and i have attached our old truck the file is called 091013_brookvale_security_proof i need something new and very modern. Using the blues colors

Target Market(s)

Security company

Industry/Entity Type

Security system

Colors
0054AA
0677BA
7BADD7
CADEEF
E8F1F8

Requirements
Must have
• same colors and logo logo
Should not have
• 091013_brookvale_security_proof the picture is our old design we want something totally new

```html
<!DOCTYPE html>
<html lang="en">
<head>
<meta charset="utf-8">
<title>Brookvale Security – Velmar QT 450 Rear Wrap</title>
<link rel="stylesheet" href="https://fonts.googleapis.com/css2?family=Montserrat:wght@600;800&family=Orbitron:wght@700&display=swap">
<style>
  :root {
    --wrap-white: #f1f1ef;
    --brand-blue: #0b5690;
    --stripe-red: #c8101a;
    --text-white: #ffffff;
  }
  * { margin: 0; padding: 0; box-sizing: border-box; }
  html, body { width: 1200px; height: 1200px; overflow: hidden; background: var(--wrap-white); }
  .rear-wrap { position: relative; width: 1200px; height: 1200px; }
  .upper-panel { position: absolute; left: 0; top: 0; width: 1200px; height: 480px; background: var(--wrap-white); }
  .accent-stripe { position: absolute; left: 0; top: 480px; width: 1200px; height: 36px; background: var(--stripe-red); }
  .lower-panel { position: absolute; left: 0; top: 530px; width: 1200px; height: 670px; background: var(--brand-blue); }

  .brand-mark { position: absolute; left: 80px; top: 140px; display: flex; align-items: center; gap: 36px; }
  .brand-dot { width: 200px; height: 200px; border-radius: 50%; background: var(--brand-blue); flex: none; }
  .brand-name {
    font-family: "Montserrat", sans-serif; font-weight: 800; font-size: 78px;
    color: var(--brand-blue); text-transform: uppercase; letter-spacing: 1px; line-height: 1;
  }

  .service-list { position: absolute; left: 140px; top: 690px; list-style: none; }
  .service-list li {
    font-family: "Orbitron", sans-serif; font-weight: 700; font-size: 38px;
    color: var(--text-white); line-height: 58px; letter-spacing: 1px;
  }
  .service-list li::before { content: "•"; margin-right: 18px; font-size: 30px; }

  .contact { position: absolute; left: 0; top: 880px; width: 1200px; text-align: center; color: var(--text-white); font-family: "Montserrat", sans-serif; }
  .contact-phone { font-weight: 800; font-size: 84px; letter-spacing: 1px; line-height: 1.05; }
  .contact-web { font-weight: 600; font-size: 54px; line-height: 1.1; }
</style>
</head>
<body>
<main class="rear-wrap">
  <div class="upper-panel">
    <div class="brand-mark">
      <span class="brand-dot"></span>
      <span class="brand-name">Brookvale Security</span>
    </div>
  </div>
  <div class="accent-stripe"></div>
  <div class="lower-panel"></div>
  <ul class="service-list">
    <li>Residencial</li>
    <li>Commercial</li>
    <li>Automotive</li>
  </ul>
  <div class="contact">
    <p class="contact-phone">613-555-0182</p>
    <p class="contact-web">www.brookvalesecurity.ca</p>
  </div>
</main>
</body>
</html>
```